RTV CRAFTED

building services
decks
pergola
renovation
extensions
general building

Target Market(s)

middle to upper class

Industry/Entity Type

building

Contact Information for Business Card

my details 0427839152 pkharlow47@mailvane.net BLD574926

Font styles to use
Serif

Colors
00AB8E
00BBA5
67D7C9
C6EFE9
E9F9F6

Requirements
Must have
• logo on the front and details on the back
Nice to have
• sharp and clean lines

```html
<!DOCTYPE html>
<html lang="en">
<head>
<meta charset="UTF-8">
<title>RTV Crafted – Business Cards</title>
<link href="https://fonts.googleapis.com/css2?family=Playfair+Display:wght@400;500;700&display=swap" rel="stylesheet">
<style>
  :root {
    --stage: #2b2b2b;
    --teal-deep: #00AB8E;
    --teal: #00BBA5;
    --teal-soft: #67D7C9;
    --mint: #C6EFE9;
    --mint-pale: #E9F9F6;
    --ink-dark: #0b3f37;
  }
  * { margin: 0; padding: 0; box-sizing: border-box; }
  html, body {
    width: 1200px; height: 900px; overflow: hidden;
    background: var(--stage);
    font-family: "Playfair Display", Georgia, serif;
  }
  .stage {
    width: 1200px; height: 900px;
    display: flex; flex-direction: column;
    align-items: center; justify-content: center; gap: 60px;
  }
  .card {
    position: relative;
    width: 600px; height: 343px;
    overflow: hidden;
    box-shadow: 0 14px 30px rgba(0,0,0,0.45);
  }
  .wordmark {
    font-weight: 700; letter-spacing: 2px;
    text-transform: uppercase;
  }

  /* Front: logo only */
  .card-front {
    background: var(--teal-deep);
    display: flex; align-items: center; justify-content: center;
  }
  .card-front .wordmark { font-size: 54px; color: var(--mint-pale); }

  /* Back: details */
  .card-back { background: var(--mint-pale); }
  .back-panel { position: absolute; inset: 0; width: 600px; height: 343px; }
  .details {
    position: absolute; left: 318px; top: 30px; right: 20px;
    color: var(--mint-pale); font-size: 14px; line-height: 20px;
  }
  .person-name { color: #ffffff; font-weight: 700; font-size: 20px; line-height: 26px; letter-spacing: 0.5px; }
  .person-role, .licence { font-weight: 500; letter-spacing: 0.5px; }
  .contact { display: flex; align-items: center; gap: 7px; }
  .contact svg { width: 12px; height: 12px; flex: none; }
  .services-title { margin-top: 6px; font-weight: 700; text-transform: uppercase; letter-spacing: 0.5px; color: #ffffff; }
  .services { list-style: none; }
  .services li { display: flex; align-items: center; gap: 8px; }
  .services li::before {
    content: ""; width: 8px; height: 8px; border-radius: 50%;
    background: var(--mint); flex: none;
  }
</style>
</head>
<body>
<main class="stage">
  <section class="card card-front" aria-label="Business card front">
    <span class="wordmark">RTV Crafted</span>
  </section>

  <section class="card card-back" aria-label="Business card back">
    <svg class="back-panel" viewBox="0 0 600 343" aria-hidden="true">
      <rect x="0" y="0" width="14" height="343" fill="var(--mint)"/>
      <line x1="40" y1="60" x2="250" y2="60" stroke="var(--teal-soft)" stroke-width="2"/>
      <line x1="40" y1="283" x2="250" y2="283" stroke="var(--teal-soft)" stroke-width="2"/>
      <polygon points="290,0 600,0 600,343 290,343 290,72 280,62 280,48 290,38" fill="var(--teal-deep)"/>
      <rect x="590" y="0" width="10" height="343" fill="var(--teal)"/>
    </svg>
    <div class="details">
      <p class="person-name">DANIEL FORBES</p>
      <p class="person-role">DIRECTOR</p>
      <p class="licence">BLD574926</p>
      <p class="contact">
        <svg viewBox="0 0 24 24"><path fill="currentColor" d="M6.6 10.8a15.1 15.1 0 0 0 6.6 6.6l2.2-2.2c.3-.3.7-.4 1-.2 1.1.4 2.3.6 3.6.6.6 0 1 .4 1 1V20c0 .6-.4 1-1 1A17 17 0 0 1 3 4c0-.6.4-1 1-1h3.5c.6 0 1 .4 1 1 0 1.3.2 2.5.6 3.6.1.3 0 .7-.2 1z"/></svg>
        <span>0427839152</span>
      </p>
      <p class="contact">
        <svg viewBox="0 0 24 24"><rect x="2.5" y="5" width="19" height="14" fill="none" stroke="currentColor" stroke-width="2.5"/><path d="M3 6l9 7 9-7" fill="none" stroke="currentColor" stroke-width="2.5"/></svg>
        <span>pkharlow47@mailvane.net</span>
      </p>
      <p class="services-title">Building services</p>
      <ul class="services">
        <li>Decks</li>
        <li>Pergola</li>
        <li>Renovation</li>
        <li>Extensions</li>
        <li>General building</li>
      </ul>
    </div>
  </section>
</main>
</body>
</html>
```